Healthy Food Healthy Brain Rack Card

We want a new 2 page (front and page) 3.67" x 8.5" rack card. This rack card is the first of a series we are creating. We will have five more eventually.

The minimum font size for the text on the front is 11 point and also for other main body text.

Use the text on the word document.

The images and layout in the word document are just sample ideas we had.

We have a subscripton to adobe stock images so prefer to get images from there or free high quality images.

The document is for older readers. Do not put text over graphics and keep it simple and easy to read with high contrast.

We are open to any color scheme, though something that conveys fresh and healthy, is good.

We want some very simple design element(s) incorporated that convey Native American communities or heritage. But NO head dress, teepee graphics, etc.

At the top, of the first page we would like a collage of healthy food images. This can include fish, chicken, fresh vegetables, berries, brown rice, etc.

On the back side, the text below the brown box on the word document with the title "mock up" can be smaller as needed.

Please remember to include the funding statement - it can be in a very small font 6/7 point.

For more information about our project, please visit https://velmorcollective.org/mind-care/

```html
<!DOCTYPE html>
<html lang="en">
<head>
<meta charset="utf-8">
<title>Healthy Food, Healthy Brain – Rack Card</title>
<link href="https://fonts.googleapis.com/css2?family=Bebas+Neue&family=Poppins:ital,wght@0,400;0,600;0,700;1,400&display=swap" rel="stylesheet">
<style>
  :root {
    --backdrop: #262626;
    --teal: #4aa9b0;
    --rose: #b15c55;
    --rose-dark: #a65a52;
    --white: #ffffff;
    --ink: #111111;
  }
  * { margin: 0; padding: 0; box-sizing: border-box; }
  html, body { width: 1200px; height: 1200px; overflow: hidden; }
  body { background: var(--backdrop); font-family: "Poppins", sans-serif; position: relative; }

  .rack-card {
    position: absolute; top: 107px; width: 425px; height: 986px;
    background: var(--white); overflow: hidden;
  }
  .rack-card--front { left: 151px; }
  .rack-card--back { left: 624px; }
  .card-waves { position: absolute; inset: 0; width: 425px; height: 986px; }
  .block { position: absolute; }

  .display-heading {
    font-family: "Bebas Neue", sans-serif; color: var(--white);
    line-height: 0.88; text-align: center;
  }

  /* front */
  .front-heading { top: 25px; left: 20px; width: 385px; font-size: 32px; }
  .food-collage {
    top: 88px; left: 33px; width: 356px; height: 225px;
    display: grid; grid-template-columns: 112px 112px 132px; grid-template-rows: 113px 112px;
  }
  .photo { display: block; width: 100%; height: 100%; }
  .photo--salmon { background: linear-gradient(135deg, #f2efe9, #f08a5d 55%, #e9e4dc); }
  .photo--rice { background: radial-gradient(circle at 50% 45%, #efe6cf, #d9ccae 60%, #f4f4f2); }
  .photo--berries { grid-column: 3; grid-row: 1 / span 2; background: linear-gradient(160deg, #3f7d3a 0%, #2a2030 25%, #c2314b 45%, #6f86a8 70%, #9fb0c8 100%); }
  .photo--vegetables { background: linear-gradient(135deg, #5a6b3a, #c8453a 45%, #d4a373 70%, #3f6b3a); }
  .photo--whitefish { background: linear-gradient(150deg, #e8d9c2, #f4efe6 40%, #c9884d 75%, #a3c46a); }
  .front-quote {
    top: 322px; left: 18px; width: 389px; text-align: center;
    font-size: 16px; line-height: 19.5px; color: var(--ink);
  }
  .front-quote q { quotes: "\201C" "\201D"; }
  .front-quote q::before, .front-quote q::after { font-weight: 700; }

  .brain-heading { top: 409px; left: 20px; width: 385px; font-size: 37px; }
  .body-copy {
    color: var(--white); font-size: 16px; line-height: 21px; text-align: justify;
  }
  .intro-copy { top: 442px; left: 29px; width: 366px; }
  .steps-heading { top: 563px; left: 29px; font-size: 24.5px; text-align: left; }
  .brain-steps {
    top: 598px; left: 29px; width: 370px; list-style: none;
    color: var(--white); font-size: 16px; line-height: 21.3px;
  }
  .brain-steps::before {
    content: ""; position: absolute; left: 7px; top: 8px; bottom: 6px;
    border-left: 1px solid rgba(255,255,255,0.8);
  }
  .brain-steps li { position: relative; padding-left: 28px; margin-bottom: 4.8px; }
  .brain-steps li::before {
    content: ""; position: absolute; left: 2px; top: 6px;
    width: 11px; height: 11px; border-radius: 50%; background: var(--white);
  }

  /* back */
  .recipe-heading { top: 14px; left: 10px; width: 405px; font-size: 62px; line-height: 0.8; }
  .recipe-subtitle {
    top: 62px; left: 10px; width: 405px; text-align: center;
    font-weight: 600; font-size: 16.3px; color: var(--white); letter-spacing: 0.1px;
  }
  .recipe-photo { top: 113px; left: 29px; width: 128px; height: 156px;
    background: linear-gradient(160deg, #f4f1ec 0%, #f07f4e 30%, #f59a6a 55%, #efe9e1 70%, #ef7a47 90%); }
  .ingredients { top: 108px; left: 173px; width: 240px; }
  .ingredients-title { font-weight: 700; font-size: 19px; color: var(--rose-dark); line-height: 22px; }
  .ingredient-line { font-size: 17px; line-height: 21px; color: var(--ink); }
  .ingredient-line--note { font-size: 14px; }
  .dot { display: inline-block; width: 9px; height: 9px; border-radius: 50%; background: var(--rose); margin: 0 4px 2px 2px; }
  .method { top: 279px; left: 29px; width: 366px; font-size: 15.6px; line-height: 19.3px; text-align: justify; color: var(--ink); }
  .community-note {
    top: 462px; left: 28px; width: 367px; height: 119px; border-radius: 6px;
    background: var(--teal); color: var(--white); text-align: center;
    font-size: 16px; line-height: 19.4px; padding: 11px 14px 0;
  }
  .org-mark { top: 593px; left: 78px; display: flex; align-items: center; gap: 12px; }
  .org-mark .org-circle { width: 64px; height: 64px; border-radius: 50%; background: var(--teal); }
  .org-mark .org-name { font-weight: 600; font-size: 19px; line-height: 21px; color: var(--teal); }

  .resources { top: 693px; left: 10px; width: 405px; text-align: center; color: var(--white); }
  .resource { margin-bottom: 9px; font-size: 16px; line-height: 18px; }
  .resource-title { font-weight: 700; font-size: 18px; line-height: 22px; margin-bottom: 1px; }
  .resource strong { font-weight: 700; }
  .funding {
    top: 913px; left: 20px; width: 385px; text-align: center;
    color: var(--white); font-size: 8.5px; line-height: 11.5px;
  }
</style>
</head>
<body>

<section class="rack-card rack-card--front" aria-label="Rack card front">
  <svg class="card-waves" viewBox="0 0 425 986" aria-hidden="true">
    <path d="M0 0 H425 V107 C330 150 200 138 0 151 Z" fill="var(--teal)"/>
    <path d="M0 412 C110 372 260 396 425 370 V986 H0 Z" fill="var(--rose)"/>
  </svg>

  <h2 class="block display-heading front-heading">Talk to your doctor about more<br>steps to healthier food choices.</h2>

  <div class="block food-collage">
    <span class="photo photo--salmon" role="img" aria-label="Fresh salmon steaks with lemon and rosemary"></span>
    <span class="photo photo--rice" role="img" aria-label="Bowl of cooked brown rice"></span>
    <span class="photo photo--berries" role="img" aria-label="Close-up of blueberry, blackberry and raspberry"></span>
    <span class="photo photo--vegetables" role="img" aria-label="Assorted fresh vegetables: peppers, carrots, mushrooms, broccoli"></span>
    <span class="photo photo--whitefish" role="img" aria-label="Grilled white fish fillet with greens"></span>
  </div>

  <p class="block front-quote"><q>Without the elk, salmon, huckleberries, shellfish, &amp; cedar trees we are nobody…</q><br>Lorna Redfern (<em>Saltwater Band</em>)</p>

  <h2 class="block display-heading brain-heading">Healthy Food, Healthy Brain</h2>
  <p class="block body-copy intro-copy">Everyone slows down as they get older, both in body &amp; mind. Eating healthier food can help your overall health, includ­ing brain health. It may also reduce your risk for memory loss &amp; problems thinking.</p>

  <h3 class="block display-heading steps-heading">Healthier steps to protect your brain:</h3>
  <ul class="block brain-steps">
    <li>Eat more vegetables, fruits,<br>whole grains, &amp; lower-fat milk</li>
    <li>Use less salt &amp; added sugar</li>
    <li>Eat more fish, chicken, turkey,<br>beans, &amp; nuts</li>
    <li>Cut down on bad fats (“saturated”<br>&amp; trans), cholesterol, &amp; red meat</li>
    <li>Buy fresh, not packaged food<br>when you can</li>
    <li>Limit how much alcohol you drink</li>
    <li>Learn your daily calorie needs for<br>your body size</li>
    <li>Take care of your mental &amp;<br>spiritual health to support your<br>physical &amp; brain health</li>
  </ul>
</section>

<section class="rack-card rack-card--back" aria-label="Rack card back">
  <svg class="card-waves" viewBox="0 0 425 986" aria-hidden="true">
    <path d="M0 0 H425 V80 C330 128 150 96 0 120 Z" fill="var(--teal)"/>
    <path d="M0 694 C120 660 300 682 425 648 V986 H0 Z" fill="var(--rose)"/>
  </svg>

  <h2 class="block display-heading recipe-heading">Make this at home</h2>
  <p class="block recipe-subtitle">GRILLED SALMON &amp; VEGGIE FOIL PACKETS</p>

  <div class="block recipe-photo" role="img" aria-label="Raw salmon steaks with rosemary and lemon"></div>

  <div class="block ingredients">
    <h3 class="ingredients-title">INGREDIENTS:</h3>
    <p class="ingredient-line"><span class="dot"></span>Salmon <span class="dot"></span>Asparagus</p>
    <p class="ingredient-line"><span class="dot"></span>Red or Green Peppers</p>
    <p class="ingredient-line ingredient-line--note"><span class="dot"></span>(Or any seasonal vegetable)</p>
    <p class="ingredient-line"><span class="dot"></span>Onion <span class="dot"></span>Lemon-sliced</p>
    <p class="ingredient-line"><span class="dot"></span>Basil <span class="dot"></span>Olive Oil</p>
    <p class="ingredient-line"><span class="dot"></span>Salt &amp; Pepper</p>
    <p class="ingredient-line"><span class="dot"></span>Garlic Powder</p>
  </div>

  <p class="block method">Cut asparagus, peppers, &amp; onion into bite-size pieces. Cut salmon into 4-6 oz pieces. Tear tin foil large enough to wrap around salmon &amp; veggies (2 layers). Add veggies &amp; salmon to foil. Drizzle with olive oil, season with salt, pepper, basil, garlic &amp; top with a piece of sliced lemon. Wrap foil tightly around food. Grill at 400 degrees for about 20 minutes. Careful opening!</p>

  <p class="block community-note">Food &amp; drink are a source of strength &amp; connection to community. A return to traditional food pathways &amp; eating local, seasonal fresh foods make healthier eating easier.</p>

  <div class="block org-mark">
    <span class="org-circle" aria-hidden="true"></span>
    <span class="org-name">VELMOR<br>COLLECTIVE</span>
  </div>

  <div class="block resources">
    <div class="resource">
      <h4 class="resource-title">About Healthier Eating</h4>
      <p>BalancedTable<br>www.<strong>balancedtable</strong>.org</p>
    </div>
    <div class="resource">
      <h4 class="resource-title">About Brain Health</h4>
      <p>Velmor Collective Center<br>for Brain Health<br>www.<strong>velmorcollective</strong>.org</p>
    </div>
    <div class="resource">
      <p>Northfield Memory Program<br><strong>https://www.northfieldmemory.org/aging</strong></p>
    </div>
  </div>

  <p class="block funding">This product is supported by the Northfield Health Fund (NHF) of the Regional Wellness Office (RWO) as part of a financial assistance award totaling $348,711 with 100 percent funded by NHF/RWO. The contents are those of the author(s) and do not necessarily represent the official views of, nor an endorsement, by NHF/RWO, or any agency.</p>
</section>

</body>
</html>
```